Brivora Collective Business Card Design

We need a business card design for Brivora Collective. We are a healthcare recruiting, wellness and education company. We partner with medical facilities to find quality candidates. We also offer free wellness courses.
The final design should communicate an emphasis on recruiting and wellness
The main purpose of the business card is to utilized it for networking events, give to hospitals, executives, VCs surgery centers and clinics. I want it to be sleek, clean, use of our brand colors and professional.

```html
<!DOCTYPE html>
<html lang="en">
<head>
<meta charset="utf-8">
<title>Brivora Collective Business Card</title>
<link rel="stylesheet" href="https://fonts.googleapis.com/css2?family=Montserrat:wght@400;500;700&display=swap">
<style>
  :root {
    --backdrop: #9a9a9a;
    --brand-green: #0d5a4c;
    --brand-green-deep: #08483d;
    --paper: #f7f7f5;
    --ink: #3a3a3a;
    --reverse: #ffffff;
  }
  html, body {
    margin: 0;
    padding: 0;
    width: 1200px;
    height: 1020px;
    overflow: hidden;
    background: var(--backdrop);
    font-family: "Montserrat", sans-serif;
  }
  .canvas {
    position: relative;
    width: 1200px;
    height: 1020px;
  }
  .card {
    position: absolute;
    left: 250px;
    width: 700px;
    height: 400px;
    box-sizing: border-box;
    box-shadow: 0 10px 28px rgba(0,0,0,0.25);
  }
  .card-front {
    top: 80px;
    background: var(--paper);
  }
  .card-back {
    top: 540px;
    background: var(--brand-green);
    display: flex;
    align-items: center;
    justify-content: center;
  }
  .name-marker {
    position: absolute;
    left: 0;
    top: 42px;
    width: 20px;
    height: 46px;
    background: var(--brand-green);
  }
  .holder {
    position: absolute;
    left: 42px;
    top: 44px;
  }
  .holder-name {
    margin: 0;
    font-size: 22px;
    font-weight: 700;
    letter-spacing: 1px;
    color: var(--brand-green);
    text-transform: uppercase;
  }
  .holder-title {
    margin: 2px 0 0;
    font-size: 15px;
    font-weight: 400;
    letter-spacing: 0.5px;
    color: var(--ink);
  }
  .address {
    position: absolute;
    left: 42px;
    top: 168px;
    margin: 0;
    font-size: 15px;
    line-height: 1.4;
    letter-spacing: 0.5px;
    color: var(--ink);
    font-style: normal;
  }
  .contact-list {
    position: absolute;
    left: 42px;
    top: 236px;
    margin: 0;
    padding: 0;
    list-style: none;
    font-size: 15px;
    letter-spacing: 0.5px;
    color: var(--ink);
  }
  .contact-list li {
    display: flex;
    align-items: center;
    gap: 10px;
    height: 27px;
  }
  .contact-icon {
    width: 14px;
    height: 14px;
    fill: var(--brand-green);
    flex: none;
  }
  .wordmark {
    position: absolute;
    right: 44px;
    top: 150px;
    display: flex;
    align-items: center;
    gap: 12px;
  }
  .wordmark-square {
    width: 26px;
    height: 26px;
    border-radius: 4px;
    background: var(--brand-green);
  }
  .wordmark-text {
    font-size: 30px;
    font-weight: 500;
    color: var(--brand-green);
    line-height: 1;
  }
  .back-wordmark {
    display: flex;
    align-items: center;
    gap: 22px;
  }
  .back-wordmark .wordmark-square {
    width: 52px;
    height: 52px;
    border-radius: 8px;
    background: var(--reverse);
  }
  .back-wordmark .wordmark-text {
    font-size: 50px;
    color: var(--reverse);
  }
</style>
</head>
<body>
<main class="canvas">
  <section class="card card-front" aria-label="Card front">
    <span class="name-marker"></span>
    <div class="holder">
      <h1 class="holder-name">Daniel Okafor</h1>
      <p class="holder-title">Owner &amp; Manager</p>
    </div>
    <address class="address">P.O. Box&nbsp; Street Name<br>Country Name AB, A5B 521</address>
    <ul class="contact-list">
      <li>
        <svg class="contact-icon" viewBox="0 0 16 16" aria-hidden="true"><path d="M1 6c0-2 3-4 7-4s7 2 7 4v1h-4V5H5v2H1z"/><rect x="3" y="8" width="10" height="6" rx="1"/></svg>
        555 210 3841
      </li>
      <li>
        <svg class="contact-icon" viewBox="0 0 16 16" aria-hidden="true"><path d="M4 1h8v14H4z M5.5 2.5v9h5v-9z" fill-rule="evenodd"/></svg>
        555-318-40276
      </li>
      <li>
        <svg class="contact-icon" viewBox="0 0 16 16" aria-hidden="true"><path d="M1 4h14v9H1z M2 5l6 4 6-4" fill-rule="evenodd"/></svg>
        info@brivoracollective.com
      </li>
      <li>
        <svg class="contact-icon" viewBox="0 0 16 16" aria-hidden="true"><circle cx="8" cy="8" r="7"/></svg>
        www.brivoracollective.com
      </li>
    </ul>
    <div class="wordmark">
      <span class="wordmark-square"></span>
      <span class="wordmark-text">Brivora Collective</span>
    </div>
  </section>

  <section class="card card-back" aria-label="Card back">
    <div class="back-wordmark">
      <span class="wordmark-square"></span>
      <span class="wordmark-text">Brivora Collective</span>
    </div>
  </section>
</main>
</body>
</html>
```